Wordpress Design for a Private Label BBQ Brand

For our new brand, we'd need a new Wordpress website. We'd prefer to run the website on Wordpress

We'd like to include the following
- space for description of the brand
- space for product portfolio (not a shop!)
- space for socials
- space for support
- space for contact

```html
<!DOCTYPE html>
<html lang="en">
<head>
<meta charset="utf-8">
<title>Emberly – Private Label BBQ Brand</title>
<link href="https://fonts.googleapis.com/css2?family=Poppins:wght@400;500;600;700&display=swap" rel="stylesheet">
<style>
:root{
  --accent:#d4461c;
  --ink:#141414;
  --muted:#333;
  --card:#f6f6f6;
  --line:#dcdcdc;
  --hero:#eef2f2;
  --white:#fff;
}
*{box-sizing:border-box;margin:0;padding:0}
html,body{width:1200px;height:4342px;overflow:hidden;background:var(--white)}
body{position:relative;font-family:'Poppins',sans-serif;color:var(--ink)}
.abs{position:absolute}
.accent{color:var(--accent)}
.btn{position:absolute;background:var(--accent);color:#fff;display:flex;align-items:center;justify-content:center;font-weight:400;border-radius:2px}
.card{position:absolute;background:var(--card)}
.ph{position:absolute;border-radius:4px}
.ph-dark{background:radial-gradient(ellipse at 40% 35%,#4a4a4a,#151515 70%)}
.ph-tool{background:linear-gradient(90deg,#9a9ea3,#d9dcdf 50%,#2a2a2a)}
.ph-steel{background:linear-gradient(180deg,#c9cdd1,#6f757b)}
.ph-round{background:radial-gradient(circle,#efe7d8 30%,#7d7d7d 55%,#1e1e1e 70%);border-radius:50%}
.tag{font-size:12px;color:var(--accent)}
.ctitle{font-size:22px;font-weight:500}
.explore{position:absolute;background:#fff;font-size:14px;font-weight:500;display:flex;align-items:center;justify-content:center;width:134px;height:42px}
.discover{position:absolute;font-size:15px;font-weight:500;display:flex;align-items:center;gap:14px}
.input{position:absolute;background:#f1f1f1;font-size:14px;padding-left:18px;display:flex;align-items:center}
.nav a{position:absolute;top:40px;font-size:16px;color:var(--ink);text-decoration:none}
.feature .rule{position:absolute;width:74px;height:2px;background:var(--ink)}
.feature h3{position:absolute;font-size:25px;font-weight:500}
.feature p{position:absolute;font-size:13px;line-height:21px;width:270px}
.partner{position:absolute;top:2528px;width:70px;height:52px;border:2px solid #888;border-radius:50%}
.tile{position:absolute;top:3160px;width:267px;height:265px;background:#fff}
.tile-label{position:absolute;top:3452px;width:267px;text-align:center;font-size:22px;font-weight:500}
.contact-card{position:absolute;top:3937px;width:304px;height:314px;background:var(--card);text-align:center}
.contact-card .icon{position:absolute;left:106px;top:62px;width:92px;height:92px;border-radius:50%;background:var(--accent);display:flex;align-items:center;justify-content:center}
.contact-card h4{position:absolute;top:208px;width:100%;font-size:21px;font-weight:600}
.contact-card p{position:absolute;top:252px;width:100%;font-size:15px}
</style>
</head>
<body>

<!-- Header -->
<header class="nav">
  <div class="abs" style="left:132px;top:36px;display:flex;align-items:center;gap:8px">
    <span style="width:22px;height:22px;border-radius:50%;background:var(--accent);display:inline-block"></span>
    <span style="font-size:30px;font-weight:700;letter-spacing:.5px">EMBERLY</span>
  </div>
  <a style="left:560px" href="#">Home</a>
  <a style="left:654px" href="#">Product</a>
  <a style="left:761px" href="#">Blog</a>
  <a style="left:842px" href="#">Contact</a>
  <div class="btn" style="left:957px;top:32px;width:116px;height:38px;font-size:15px">Portfolio</div>
</header>

<!-- Hero -->
<section class="hero">
  <svg class="abs" style="left:0;top:420px" width="1200" height="347" viewBox="0 0 1200 347">
    <path d="M0 110 C200 60 360 150 560 100 C760 50 900 40 1200 90 L1200 347 L0 347Z" fill="#f3f6f6"/>
    <path d="M0 180 C180 120 360 200 600 150 C820 110 1000 150 1200 130 L1200 347 L0 347Z" fill="var(--hero)"/>
  </svg>
  <h1 class="abs" style="left:130px;top:230px;font-size:64px;line-height:66px;font-weight:700">Private Label <span class="accent">BBQ</span><br>Brand</h1>
  <p class="abs" style="left:131px;top:395px;width:430px;font-size:15px;line-height:24px">Sed ut perspiciatis unde omnis iste natus error sit accusantium laudantium totam rem aperiam eaque ipsa quae.</p>
  <div class="btn" style="left:131px;top:508px;width:201px;height:55px;font-size:22px">Learn More</div>
  <div class="ph ph-dark" role="img" aria-label="Black ceramic kamado grill on tripod stand" style="left:725px;top:125px;width:315px;height:595px;border-radius:48% 48% 10% 10%"></div>
</section>

<!-- Features -->
<section class="feature">
  <div class="rule" style="left:131px;top:872px"></div>
  <h3 style="left:131px;top:893px">Fastest Support</h3>
  <p style="left:131px;top:943px">Lorem insum dolor amet consec tetur adiriscin elit eiusmod temsor incididunt.</p>
  <div class="rule" style="left:475px;top:872px"></div>
  <h3 style="left:475px;top:893px">Daily Freebies</h3>
  <p style="left:475px;top:943px">Lorem insum dolor amet consec tetur adiriscin elit eiusmod temsor incididunt.</p>
  <div class="rule" style="left:820px;top:872px"></div>
  <h3 style="left:820px;top:893px">Reliable Pricings</h3>
  <p style="left:820px;top:943px">Lorem insum dolor amet consec tetur adiriscin elit eiusmod temsor incididunt.</p>
  <div class="abs" style="left:131px;top:1058px;width:942px;height:1px;background:var(--line)"></div>
</section>

<!-- Portfolio -->
<section class="portfolio">
  <h2 class="abs" style="left:131px;top:1166px;font-size:30px;font-weight:600">Label <span class="accent">BBQ</span> Brand</h2>
  <div class="abs" style="left:432px;top:1164px;width:1px;height:44px;background:var(--line)"></div>
  <p class="abs" style="left:471px;top:1165px;width:600px;font-size:13px;line-height:21px">Exercita tionem ullam cornoris suscihit labori aliruid conseruatur autem resreh enderit volustate velit esse nihil conser illum dolorem fusiat voluntas nulla sariatur.</p>

  <div class="card" style="left:133px;top:1262px;width:290px;height:435px">
    <div class="tag abs" style="left:18px;top:24px">45 item</div>
    <div class="ctitle abs" style="left:18px;top:42px">New Products</div>
    <div class="ph ph-tool" role="img" aria-label="Set of grill tongs, fork and spatula" style="left:60px;top:135px;width:180px;height:200px;background:linear-gradient(180deg,#c4c8cc 40%,#151515)"></div>
    <div class="discover" style="left:18px;top:385px">Discover More <span>⟶</span></div>
  </div>
  <div class="card" style="left:133px;top:1732px;width:290px;height:195px">
    <div class="tag abs" style="left:15px;top:20px">45 item</div>
    <div class="ctitle abs" style="left:15px;top:38px">New Products</div>
    <div class="ph ph-dark" role="img" aria-label="Portable charcoal grill base" style="left:68px;top:85px;width:158px;height:90px"></div>
  </div>

  <div class="card" style="left:458px;top:1262px;width:290px;height:244px">
    <div class="ctitle abs" style="width:100%;text-align:center;top:34px">Latest Products</div>
    <div class="ph ph-steel" role="img" aria-label="Aluminium grill tool case" style="left:62px;top:85px;width:168px;height:70px"></div>
    <div class="explore" style="left:78px;top:185px">Explore all</div>
  </div>
  <div class="card" style="left:458px;top:1540px;width:290px;height:387px">
    <div class="ctitle abs" style="left:16px;top:28px">Latest Products</div>
    <div class="ph ph-tool" role="img" aria-label="Serrated grill spatula blade" style="left:110px;top:60px;width:70px;height:245px;background:linear-gradient(160deg,#aaa,#222)"></div>
    <div class="explore" style="left:78px;top:328px">Explore all</div>
  </div>

  <div class="card" style="left:783px;top:1262px;width:290px;height:340px">
    <div class="tag abs" style="left:30px;top:24px">45 item</div>
    <div class="ctitle abs" style="left:30px;top:42px">New Products</div>
    <div class="ph ph-tool" role="img" aria-label="Pair of grill tool handles" style="left:85px;top:95px;width:115px;height:140px;background:linear-gradient(180deg,#cfd3d6,#3c4046 70%,#111)"></div>
    <div class="discover" style="left:25px;top:298px">Discover More <span>⟶</span></div>
  </div>
  <div class="card" style="left:783px;top:1636px;width:290px;height:291px">
    <div class="ph ph-round" role="img" aria-label="Round portable kettle grill" style="left:70px;top:62px;width:150px;height:150px"></div>
    <div class="tag abs" style="left:25px;top:232px">45 item</div>
    <div class="ctitle abs" style="left:25px;top:250px">New Products</div>
  </div>

  <div class="card" style="left:133px;top:1970px;width:615px;height:248px">
    <div class="ph ph-tool" role="img" aria-label="Stainless steel grill spatula" style="left:72px;top:105px;width:290px;height:40px"></div>
    <div class="tag abs" style="left:430px;top:62px">45 item</div>
    <div class="ctitle abs" style="left:430px;top:80px">New Products</div>
    <div class="explore" style="left:430px;top:144px">Explore all</div>
  </div>
  <div class="card" style="left:783px;top:1970px;width:290px;height:475px">
    <div class="tag abs" style="left:30px;top:32px">45 item</div>
    <div class="ctitle abs" style="left:30px;top:50px">New Products</div>
    <div class="ph ph-tool" role="img" aria-label="Stainless steel grill tongs" style="left:115px;top:118px;width:60px;height:258px;background:linear-gradient(180deg,#d2d5d8 45%,#1a1a1a 70%,#9a9ea3)"></div>
    <div class="discover" style="left:25px;top:420px">Discover More <span>⟶</span></div>
  </div>

  <h2 class="abs" style="left:128px;top:2266px;font-size:31px;font-weight:600">Get daily update</h2>
  <p class="abs" style="left:130px;top:2320px;width:600px;font-size:13px;line-height:21px">Exercita tionem ullam cornoris suscihit labori aliruid conseruatur autem resreh enderit volustate velit esse nihil conser illum dolorem fusiat voluntas nulla sariatur.</p>
  <div class="input" style="left:131px;top:2392px;width:382px;height:52px">Email</div>
  <div class="btn" style="left:531px;top:2392px;width:217px;height:52px;font-size:15px">Subscribe</div>
</section>

<!-- Partners -->
<section class="partners">
  <div class="partner" style="left:133px"></div>
  <div class="partner" style="left:350px;border-radius:8px"></div>
  <div class="partner" style="left:567px;border-radius:8px"></div>
  <div class="partner" style="left:783px"></div>
  <div class="partner" style="left:1000px"></div>
  <div class="abs" style="left:131px;top:2655px;width:942px;height:1px;background:var(--line)"></div>
</section>

<!-- Testimonial -->
<section class="testimonial">
  <h2 class="abs" style="left:128px;top:2770px;font-size:33px;line-height:36px;font-weight:600">Last<br>Comment</h2>
  <div class="abs" role="img" aria-label="Customer portrait" style="left:345px;top:2760px;width:104px;height:104px;border-radius:50%;background:radial-gradient(circle at 50% 40%,#d8c2ad,#8a7462)"></div>
  <p class="abs" style="left:467px;top:2762px;width:350px;font-size:13px;line-height:21px">Lorem insum dolor amet consec tetur adiriscin elit eiusmod temsor incididunt masna alirua enim veniam nostrud exerci tation ullamco aliruis conseruat irure dolor renrehen derit volustate velit esse cillum dolore funiat nulla sariatur.</p>
  <div class="abs" style="right:127px;top:2800px;font-size:18px;font-weight:600;display:flex;gap:10px;align-items:center"><span class="accent" style="font-size:34px;line-height:20px;font-weight:700">”</span>Daniel Hart</div>
</section>

<!-- Newbies -->
<section class="newbies">
  <div class="card" style="left:133px;top:2972px;width:940px;height:580px"></div>
  <h2 class="abs" style="left:150px;top:3033px;font-size:30px;font-weight:600">Newbies</h2>
  <div class="abs" style="left:368px;top:3032px;width:1px;height:44px;background:var(--line)"></div>
  <p class="abs" style="left:446px;top:3033px;width:440px;font-size:13px;line-height:21px">Exercita tionem ullam cornoris suscihit labori aliruid conseruatur autem resreh enderit volustate velit esse nihil</p>
  <div class="btn" style="left:911px;top:3027px;width:146px;height:53px;font-size:15px">Portfolio</div>
  <div class="tile" style="left:174px"><div class="ph ph-dark" role="img" aria-label="Portable charcoal grill" style="left:20px;top:70px;width:227px;height:130px"></div></div>
  <div class="tile" style="left:471px"><div class="ph ph-steel" role="img" aria-label="Open case of grill tools" style="left:50px;top:50px;width:167px;height:160px;background:linear-gradient(180deg,#3a3a3a,#111)"></div></div>
  <div class="tile" style="left:768px"><div class="ph ph-round" role="img" aria-label="Round kettle grill" style="left:50px;top:40px;width:167px;height:167px"></div></div>
  <div class="tile-label" style="left:174px">New Products</div>
  <div class="tile-label" style="left:471px">New Products</div>
  <div class="tile-label" style="left:768px">New Products</div>
</section>

<!-- Newsletter -->
<section class="newsletter">
  <h2 class="abs" style="left:0;width:1200px;text-align:center;top:3655px;font-size:30px;font-weight:600">Ratione Tatem Setui Nesciun!</h2>
  <p class="abs" style="left:230px;width:740px;text-align:center;top:3708px;font-size:13px;line-height:21px">Exercita tionem ullam cornoris suscihit labori aliruid conseruatur autem resreh enderit volustate velit esse nihil conser illum dolorem fusiat voluntas nulla sariatur.</p>
  <div class="input" style="left:292px;top:3780px;width:384px;height:52px">Email</div>
  <div class="btn" style="left:694px;top:3780px;width:216px;height:52px;font-size:15px">Subscribe</div>
</section>

<!-- Contact -->
<section class="contact">
  <div class="contact-card" style="left:124px">
    <div class="icon"><svg width="48" height="34" viewBox="0 0 48 34" fill="none" stroke="#fff" stroke-width="3"><rect x="2" y="2" width="44" height="30"/><path d="M2 2 L24 20 L46 2 M2 32 L18 16 M46 32 L30 16"/></svg></div>
    <h4>Email</h4><p>hello@emberly.com</p>
  </div>
  <div class="contact-card" style="left:450px">
    <div class="icon"><svg width="40" height="50" viewBox="0 0 40 50"><path d="M20 2 C9 2 2 10 2 20 C2 33 20 48 20 48 C20 48 38 33 38 20 C38 10 31 2 20 2Z" fill="#fff"/><circle cx="20" cy="19" r="7" fill="var(--accent)"/></svg></div>
    <h4>Address</h4><p>Excepteur occaecat cupidatat.</p>
  </div>
  <div class="contact-card" style="left:776px">
    <div class="icon"><svg width="44" height="44" viewBox="0 0 24 24"><path fill="#fff" d="M6.6 10.8a15.1 15.1 0 0 0 6.6 6.6l2.2-2.2c.3-.3.7-.4 1-.2 1.1.4 2.3.6 3.6.6.6 0 1 .4 1 1V20c0 .6-.4 1-1 1A17 17 0 0 1 3 4c0-.6.4-1 1-1h3.5c.6 0 1 .4 1 1 0 1.3.2 2.5.6 3.6.1.3 0 .7-.2 1z"/></svg></div>
    <h4>Phone</h4><p>0000 - 1111 2222 3333</p>
  </div>
</section>

</body>
</html>
```